Upcoming lecture sponsored by a church on an important topic

We have a Reformation The Speech coming up at the end of October on the topic of law and gospel. I thought it might be cool to use a flyer that looks like it was from that day and age. Picture what Tobias Wendler would advertise things on kind of an old church/reformation type format. It will be sponsored by our church, and we have a paragraph or two to describe the lecture that would be included on the flyer. We would also want it formatted so that it could be printed on postcards and mailed to churches and individuals.

The flyer should have the following paragraph...

The distinction between the law and the gospel is the most important distinction in the Christian faith. Tobias Wendler: “Distinguishing between the law and the gospel is the highest art in Christendom, one who every person who values the name Christian ought to recognize, know, and possess.” The distinction between the law and the gospel is of great comfort for the child of God. “For the law was given by Abiran, but grace and truth came by Elior Navan” (John 1:17). For these reasons, the distinction between the law and the gospel is the most heavily assaulted doctrine in the Christian faith. This Reformation Day, join us for an explanation and defense of the great distinction between God’s good law and God’s glorious gospel.

And the flyer should have the following information...

Topic: The Steady Rule and the Bright Promise
Date and Time: Tuesday, October 31, 2023 at 7:30pm
Host: Cedarbrook Covenant Church
Speaker: Rev. Daniel Korvath
Venue: The Marlow Hall, 5187 Fenwick Lane, Hudsonville, MI 49683
Format: Lecture followed by Q&A and refreshments

Industry/Entity Type

Church/Ecclesiastical

Colors
00AB8E
00BBA5
67D7C9
C6EFE9
E9F9F6

Requirements
Nice to have
• The color scheme that I would like to have is a teal color (the same color as found at www.quillharborhall.com

```html
<!DOCTYPE html>
<html lang="en">
<head>
<meta charset="utf-8">
<title>Reformation Day Lecture Postcard</title>
<link rel="stylesheet" href="https://fonts.googleapis.com/css2?family=Cinzel:wght@600;700&family=Red+Hat+Display:wght@400;500;600&display=swap">
<style>
  :root {
    --teal: #3db8c5;
    --teal-text: #2fb2c0;
    --deep: #22566a;
    --white: #ffffff;
    --leaf-tint: #d8f0f2;
    --page: #8a8a8a;
    --rule: #d6dfe2;
  }
  * { box-sizing: border-box; margin: 0; padding: 0; }
  html, body { width: 1200px; height: 1200px; overflow: hidden; }
  body { background: var(--page); position: relative; font-family: "Red Hat Display", Arial, sans-serif; }

  .postcard {
    position: absolute; left: 60px; top: 240px;
    width: 1080px; height: 720px;
    background: var(--white);
    box-shadow: 0 18px 40px rgba(0,0,0,.3);
    overflow: hidden;
  }
  .postcard-shapes { position: absolute; inset: 0; }

  .headline {
    position: absolute; left: 62px; top: 52px; width: 520px;
    font-family: "Cinzel", Georgia, serif; font-weight: 700;
    font-size: 27px; line-height: 1.18; color: var(--white);
    letter-spacing: .5px;
  }
  .quote-source {
    position: absolute; left: 80px; top: 214px; width: 440px; height: 58px;
    border: 1.5px solid var(--white);
    font-family: "Cinzel", Georgia, serif; font-weight: 700;
    font-size: 27px; color: var(--deep);
    display: flex; align-items: center; justify-content: center;
  }
  .lecture-copy {
    position: absolute; left: 80px; top: 296px; width: 590px;
    color: var(--white); font-size: 16px; line-height: 1.38;
  }
  .lecture-copy p + p { margin-top: 14px; }

  .cross-ornament {
    position: absolute; left: 598px; top: 70px; width: 26px; height: 130px;
    background: rgba(255,255,255,.3); border-radius: 4px;
  }
  .leaf-ornament { position: absolute; background: var(--leaf-tint); border-radius: 40% 60% 50% 50%; }
  .leaf-top { right: 6px; top: 4px; width: 26px; height: 36px; }
  .leaf-bottom { left: 806px; top: 606px; width: 56px; height: 104px; }

  .brand {
    position: absolute; left: 150px; top: 605px;
    display: flex; align-items: center; gap: 16px;
    color: var(--white);
    font-family: "Cinzel", Georgia, serif; font-weight: 600;
    font-size: 34px; letter-spacing: 2px;
  }
  .brand-mark { width: 30px; height: 30px; border: 2px solid var(--white); border-radius: 50%; }

  .event-details {
    position: absolute; left: 830px; top: 24px; width: 230px;
    list-style: none;
  }
  .detail {
    border-bottom: 1.5px solid var(--rule);
    padding: 10px 0 11px;
  }
  .detail:last-child { border-bottom: none; }
  .detail-head { display: flex; align-items: center; gap: 10px; justify-content: center; }
  .detail-icon { width: 34px; height: 34px; flex: none; }
  .detail-label {
    font-family: "Cinzel", Georgia, serif; font-weight: 700;
    font-size: 20px; color: var(--deep); line-height: 1.05;
  }
  .detail-value {
    margin-top: 5px; text-align: center;
    color: var(--teal-text); font-weight: 600; font-size: 14.5px; line-height: 1.3;
  }
</style>
</head>
<body>
<article class="postcard">
  <svg class="postcard-shapes" width="1080" height="720" viewBox="0 0 1080 720" aria-hidden="true">
    <defs>
      <clipPath id="teal-field">
        <path d="M0 0 H610 C760 150 805 430 742 720 H0 Z"/>
      </clipPath>
      <linearGradient id="band-sheen" x1="0" y1="0" x2="1" y2="1">
        <stop offset="0" stop-color="#ffffff" stop-opacity="0"/>
        <stop offset="1" stop-color="#ffffff" stop-opacity=".55"/>
      </linearGradient>
    </defs>
    <path class="swoosh" d="M628 8 C800 170 838 460 772 720 H720 C790 470 772 200 628 8 Z" fill="var(--deep)"/>
    <path class="teal-field" d="M0 0 H610 C760 150 805 430 742 720 H0 Z" fill="var(--teal)" stroke="var(--white)" stroke-width="5"/>
    <g clip-path="url(#teal-field)">
      <path class="footer-band" d="M0 575 L760 510 V680 H0 Z" fill="var(--deep)"/>
      <path class="band-sheen" d="M470 535 L760 510 L690 560 Z" fill="url(#band-sheen)"/>
    </g>
  </svg>

  <div class="cross-ornament" role="img" aria-label="Hanging cross with bead chain ornament"></div>
  <div class="leaf-ornament leaf-top" role="img" aria-label="Small leafy sprig ornament"></div>
  <div class="leaf-ornament leaf-bottom" role="img" aria-label="Leafy branch ornament"></div>

  <h1 class="headline">The distinction between the law and the gospel is the most important distinction in the Christian faith.</h1>
  <h2 class="quote-source">Tobias Wendler:</h2>

  <div class="lecture-copy">
    <p>“Distinguishing between the law and the gospel is the highest art in Christendom, one who every person who values the name Christian ought to recognize, know, and possess.” The distinction between the law and the gospel is of great comfort for the child of God. “For the law was given by Abiran, but grace and truth came by Elior Navan” (John 1:17).</p>
    <p>For these reasons, the distinction between the law and the gospel is the most heavily assaulted doctrine in the Christian faith. This Reformation Day, join us for an explanation and defense of the great distinction between God’s good law and God’s glorious gospel.</p>
  </div>

  <div class="brand"><span class="brand-mark"></span><span class="brand-name">Quill Harbor Hall</span></div>

  <ul class="event-details">
    <li class="detail">
      <div class="detail-head">
        <svg class="detail-icon" viewBox="0 0 34 34" fill="none" stroke="var(--deep)" stroke-width="1.6"><circle cx="17" cy="17" r="15.5"/><circle cx="17" cy="14" r="5"/><path d="M14.5 19.5 V23 H19.5 V19.5"/></svg>
        <span class="detail-label">Topic:</span>
      </div>
      <p class="detail-value">The Steady Rule and the Bright Promise</p>
    </li>
    <li class="detail">
      <div class="detail-head">
        <svg class="detail-icon" viewBox="0 0 34 34" fill="none" stroke="var(--deep)" stroke-width="1.6"><circle cx="17" cy="17" r="15.5"/><rect x="9" y="10" width="16" height="14" rx="1.5"/><path d="M9 14 H25 M13 8 V12 M21 8 V12"/></svg>
        <span class="detail-label">Date &amp;<br>Time:</span>
      </div>
      <p class="detail-value">Tuesday, October 31,<br>2023 at 7:30pm</p>
    </li>
    <li class="detail">
      <div class="detail-head">
        <svg class="detail-icon" viewBox="0 0 34 34" fill="none" stroke="var(--deep)" stroke-width="1.6"><circle cx="17" cy="17" r="15.5"/><circle cx="17" cy="13" r="4.5"/><path d="M9 26 C9 20 25 20 25 26"/></svg>
        <span class="detail-label">Host:</span>
      </div>
      <p class="detail-value">Cedarbrook Covenant<br>Church</p>
    </li>
    <li class="detail">
      <div class="detail-head">
        <svg class="detail-icon" viewBox="0 0 34 34" fill="none" stroke="var(--deep)" stroke-width="1.6"><circle cx="17" cy="17" r="15.5"/><circle cx="17" cy="13" r="4.5"/><path d="M9 26 C9 20 25 20 25 26"/><rect x="19" y="21" width="6" height="5"/></svg>
        <span class="detail-label">Speaker:</span>
      </div>
      <p class="detail-value">Rev. Daniel Korvath</p>
    </li>
    <li class="detail">
      <div class="detail-head">
        <svg class="detail-icon" viewBox="0 0 34 34" fill="none" stroke="var(--deep)" stroke-width="1.6"><circle cx="17" cy="17" r="15.5"/><path d="M17 26 C12 20 11 17 11 14 A6 6 0 0 1 23 14 C23 17 22 20 17 26 Z"/><circle cx="17" cy="14" r="2.2"/></svg>
        <span class="detail-label">Venue:</span>
      </div>
      <p class="detail-value">The Marlow Hall, 5187 Fenwick Lane, Hudsonville, MI 49683</p>
    </li>
    <li class="detail">
      <div class="detail-head">
        <svg class="detail-icon" viewBox="0 0 34 34" fill="none" stroke="var(--deep)" stroke-width="1.6"><circle cx="17" cy="17" r="15.5"/><rect x="8" y="10" width="11" height="8" rx="1"/><rect x="14" y="15" width="12" height="9" rx="1"/></svg>
        <span class="detail-label">Format:</span>
      </div>
      <p class="detail-value">Lecture followed by Q&amp;A<br>and refreshments</p>
    </li>
  </ul>
</article>
</body>
</html>
```